Halvern Ridge Plants and Nursery needs a business street sign.

I have three businesses located at the same address: The Halvern Ridge Plants & Nursery, The Marrow Stall, and The Brackett Commons. I am looking for a 4’ x 8’ street sign to represent all three businesses as one retail experience. It needs to be eye catching yet simple enough that people can fully read it while driving by. I have logos for the greenhouse and village however I do not have anything for The Marrow Stall. I’m looking for some type of font that’s similar or in between the two attached logos for The Marrow Stall.

Requirements
Must have
• Horizontal Sign, Eye catching, yet simple design so people see it while driving by.
Nice to have
• Horizontal Sign
Should not have
• I’m open to the design being both vertical and horizontal. Please provide both options

```html
<!DOCTYPE html>
<html lang="en">
<head>
<meta charset="utf-8">
<title>Halvern Ridge Plants and Nursery – Street Sign</title>
<link rel="stylesheet" href="https://fonts.googleapis.com/css2?family=Questrial&family=Great+Vibes&display=swap">
<style>
  :root {
    --page-bg: #dedede;
    --sign-bg: #000000;
    --nursery-green: #2fb44a;
    --commons-green: #80d48b;
    --script-white: #ffffff;
    --bloom-orange: #f07a3c;
    --bloom-coral: #e0444f;
    --garland-pink: #d24fc4;
    --garland-deep: #a92ea4;
    --stem-green: #4cc35a;
  }
  * { box-sizing: border-box; margin: 0; padding: 0; }
  html, body {
    width: 896px;
    height: 1200px;
    overflow: hidden;
    background: var(--page-bg);
  }
  .street-sign {
    position: absolute;
    left: 38px;
    top: 395px;
    width: 820px;
    height: 410px;
    background: var(--sign-bg);
    overflow: hidden;
    box-shadow: 0 10px 28px rgba(0,0,0,0.35);
  }
  .nursery-name {
    position: absolute;
    left: 24px;
    top: 40px;
    width: 240px;
    text-align: right;
    font-family: "Questrial", sans-serif;
    font-weight: 400;
    color: var(--nursery-green);
    line-height: 1;
  }
  .nursery-name .line-top { display: block; font-size: 30px; }
  .nursery-name .line-mid { display: block; font-size: 17px; letter-spacing: 0.5px; margin-top: 6px; }
  .nursery-name .line-bottom { display: block; font-size: 40px; margin-top: 2px; }
  .commons-name {
    position: absolute;
    left: 540px;
    top: 28px;
    width: 252px;
    text-align: right;
    font-family: "Questrial", sans-serif;
    font-weight: 400;
    color: var(--commons-green);
    line-height: 0.95;
  }
  .commons-name .line-top { display: block; font-size: 30px; padding-right: 110px; }
  .commons-name .line-mid { display: block; font-size: 46px; }
  .commons-name .line-bottom { display: block; font-size: 46px; }
  .bloom-cluster {
    position: absolute;
    left: 338px;
    top: 2px;
    width: 158px;
    height: 158px;
  }
  .garland {
    position: absolute;
    left: 0;
    top: 0;
    width: 820px;
    height: 410px;
  }
  .stall-name {
    position: absolute;
    left: 160px;
    top: 278px;
    width: 500px;
    text-align: center;
    font-family: "Great Vibes", cursive;
    color: var(--script-white);
    line-height: 0.85;
  }
  .stall-name .article { display: block; font-size: 62px; padding-left: 40px; }
  .stall-name .title { display: block; font-size: 72px; }
</style>
</head>
<body>
  <section class="street-sign">
    <svg class="garland" viewBox="0 0 820 410" role="img" aria-label="Watercolour garland of pink blossoms with green stems arching across the sign">
      <defs>
        <linearGradient id="garlandTone" x1="0" y1="0" x2="1" y2="0">
          <stop offset="0" stop-color="var(--garland-deep)"/>
          <stop offset="0.5" stop-color="var(--garland-pink)"/>
          <stop offset="1" stop-color="var(--garland-deep)"/>
        </linearGradient>
      </defs>
      <path d="M -10 372 C 120 300, 220 250, 330 222 C 430 196, 520 190, 620 230 C 700 262, 770 320, 830 372"
            fill="none" stroke="url(#garlandTone)" stroke-width="48" stroke-linecap="round"/>
    </svg>

    <svg class="bloom-cluster" viewBox="0 0 158 158" role="img" aria-label="Illustrated bouquet of orange and coral blossoms with green leaves">
      <defs>
        <radialGradient id="bloomTone" cx="0.5" cy="0.5" r="0.5">
          <stop offset="0" stop-color="var(--bloom-coral)"/>
          <stop offset="1" stop-color="var(--bloom-orange)"/>
        </radialGradient>
      </defs>
      <ellipse cx="79" cy="79" rx="62" ry="76" fill="url(#bloomTone)"/>
    </svg>

    <h1 class="nursery-name">
      <span class="line-top">The Halvern Ridge</span>
      <span class="line-mid">PLANTS</span>
      <span class="line-bottom">&amp; Nursery</span>
    </h1>

    <h2 class="commons-name">
      <span class="line-top">The</span>
      <span class="line-mid">Brackett</span>
      <span class="line-bottom">Commons</span>
    </h2>

    <h2 class="stall-name">
      <span class="article">The</span>
      <span class="title">Marrow Stall</span>
    </h2>
  </section>
</body>
</html>
```